Business card for a Exhibition booth fabrication company

Hi. My company would like to change our corporate name card. We are an events and Exhibition stand builder company. We would like our corporate name card to resonate what we do. I need someone to create something unique that relates to the industry that I am in. The graphic designer should be creative to incorporate the elements of my industry and try to blend in well in the design of the card. Our aim is to ensure that we are unique and our card can look different from our competitors.
Updates

The decision maker was very busy and didnt had time to make this decision

Target Market(s)

Marketing and events manager from all companies

Contact Information for Business Card

The business card should have the following details:
Name
Job Title
Email
Website

Colors

Designer to choose colors to be used in the design.

Requirements
Must have
• The card must be look something that is relevant to the service that I am providing. My website is: www.velmora-builds.com
• You can see my website to get more information on what service that I am doing
Nice to have
• On the back of my card, I would like to have a globe image with the incorporation of my company logo. This is to indicate that my services can be done in any part of the world.

```html
<!DOCTYPE html>
<html lang="en">
<head>
<meta charset="utf-8">
<title>Velmora Business Card</title>
<link href="https://fonts.googleapis.com/css2?family=PT+Sans:wght@400;700&display=swap" rel="stylesheet">
<style>
  :root {
    --brand-red: #e5222a;
    --brand-red-deep: #d81d24;
    --brand-red-soft: #ef4a4f;
    --band-grey: #646567;
    --paper-white: #ffffff;
  }
  html, body {
    margin: 0;
    padding: 0;
    overflow: hidden;
    background: var(--paper-white);
  }
  .card {
    position: relative;
    width: 1200px;
    height: 726px;
    overflow: hidden;
    font-family: "PT Sans", Tahoma, sans-serif;
    color: var(--paper-white);
    background: var(--brand-red);
  }
  .card__backdrop {
    position: absolute;
    inset: 0;
    width: 1200px;
    height: 726px;
    display: block;
  }
  .card__brand {
    position: absolute;
    left: 28px;
    top: 180px;
    margin: 0;
    font-size: 66px;
    font-weight: 400;
    line-height: 1;
    color: var(--paper-white);
  }
  .card__identity {
    position: absolute;
    left: 0;
    width: 1200px;
    top: 272px;
    text-align: center;
    padding-left: 0;
  }
  .card__name {
    margin: 0 0 0 0;
    font-size: 104px;
    font-weight: 400;
    line-height: 1;
  }
  .card__title {
    margin: 10px 0 0 0;
    font-size: 58px;
    font-weight: 400;
    line-height: 1;
  }
  .card__contacts {
    position: absolute;
    right: 35px;
    top: 592px;
    margin: 0;
    padding: 0;
    list-style: none;
  }
  .contact {
    display: flex;
    align-items: center;
    justify-content: flex-end;
    height: 50px;
    font-size: 30px;
    letter-spacing: 0.3px;
  }
  .contact__icon {
    width: 30px;
    height: 30px;
    margin-right: 26px;
    flex: none;
  }
</style>
</head>
<body>
  <main class="card">
    <svg class="card__backdrop" viewBox="0 0 1200 726" aria-hidden="false">
      <defs>
        <linearGradient id="venue-tone" x1="0" y1="0" x2="1" y2="1">
          <stop offset="0" stop-color="var(--brand-red-deep)"/>
          <stop offset="0.55" stop-color="var(--brand-red-soft)"/>
          <stop offset="1" stop-color="var(--brand-red)"/>
        </linearGradient>
      </defs>
      <rect class="venue-photo" role="img" aria-label="Red-tinted photograph of an exhibition hall with built booths" x="0" y="0" width="1200" height="640" fill="url(#venue-tone)"/>
      <polygon class="contact-band" points="0,628 1200,517 1200,726 0,726" fill="var(--band-grey)"/>
    </svg>

    <p class="card__brand">Velmora</p>

    <section class="card__identity">
      <h1 class="card__name">Name</h1>
      <p class="card__title">Job Title</p>
    </section>

    <ul class="card__contacts">
      <li class="contact contact--email">
        <svg class="contact__icon" viewBox="0 0 30 30" aria-hidden="true">
          <rect x="4" y="8" width="22" height="15" fill="none" stroke="var(--paper-white)" stroke-width="2"/>
          <polyline points="4,8 15,17 26,8" fill="none" stroke="var(--paper-white)" stroke-width="2"/>
          <line x1="4" y1="23" x2="12" y2="15" stroke="var(--paper-white)" stroke-width="2"/>
          <line x1="26" y1="23" x2="18" y2="15" stroke="var(--paper-white)" stroke-width="2"/>
        </svg>
        <span>info@velmora-builds.com</span>
      </li>
      <li class="contact contact--web">
        <svg class="contact__icon" viewBox="0 0 30 30" aria-hidden="true">
          <circle cx="15" cy="15" r="10" fill="none" stroke="var(--paper-white)" stroke-width="2.5"/>
        </svg>
        <span>www.velmora-builds.com</span>
      </li>
    </ul>
  </main>
</body>
</html>
```